Business card for massage therapy company called Brook Fern Wellness

Need business card for massage therapy company called Brook Fern Wellness. Would like my logo on the front and the back of the card I have 3 options of logos and you can play with what looks better.

Would like this information displayed on the back of the card:

Marcus Ellery
Licensed Massage Therapist
321-555-0147
brookfern-example.com
brookfern_rest_

```html
<!DOCTYPE html>
<html lang="en">
<head>
<meta charset="utf-8">
<title>Brook Fern Wellness – Business Card</title>
<link rel="stylesheet" href="https://fonts.googleapis.com/css2?family=Alex+Brush&family=Lexend:wght@300;400&display=swap">
<style>
  :root {
    --backdrop: #d6d6d6;
    --card-white: #ffffff;
    --sage: #707a5f;
    --sage-soft: #7c866b;
    --tan: #c4996f;
    --tan-dark: #a07a55;
    --tan-text: #c29470;
    --grey-text: #6a6b63;
    --ink: #1d1d1b;
    --white: #ffffff;
  }
  * { margin: 0; padding: 0; box-sizing: border-box; }
  html, body {
    width: 1200px; height: 1200px; overflow: hidden;
    background: var(--backdrop);
  }
  .canvas { position: relative; width: 1200px; height: 1200px; }

  .card {
    position: absolute; top: 166px;
    width: 495px; height: 866px; overflow: hidden;
  }
  .card--front { left: 84px; background: var(--card-white); }
  .card--back { left: 622px; background: var(--sage); }

  /* Front */
  .brand-name {
    position: absolute; top: 112px; left: 0; width: 100%;
    text-align: center;
    font-family: "Lexend", sans-serif; font-weight: 300;
    font-size: 36px; letter-spacing: 2px;
    color: var(--sage);
  }
  .person-name {
    position: absolute; top: 360px; left: 0; width: 100%;
    text-align: center;
    font-family: "Alex Brush", cursive;
    font-size: 66px; color: var(--tan-text);
  }
  .person-title {
    position: absolute; top: 474px; left: 0; width: 100%;
    text-align: center;
    font-family: "Lexend", sans-serif; font-weight: 300;
    font-size: 20px; color: var(--grey-text);
  }
  .contact-band {
    position: absolute; top: 590px; left: 0;
    width: 100%; height: 176px; background: var(--sage);
  }
  .ribbon { position: absolute; top: 569px; left: 34px; width: 72px; height: 222px; }
  .contact-list {
    position: absolute; top: 627px; left: 81px;
    list-style: none;
    font-family: "Lexend", sans-serif; font-weight: 300;
    font-size: 22px; color: var(--white);
  }
  .contact-item { display: flex; align-items: center; height: 35px; }
  .contact-icon { width: 14px; height: 14px; margin-right: 41px; }

  /* Back */
  .foliage-area {
    position: absolute; left: 0; top: 0; width: 100%; height: 100%;
    background: linear-gradient(160deg, rgba(124,134,107,0) 25%, rgba(124,134,107,0.55) 70%, rgba(124,134,107,0.25) 100%);
  }
  .brand-circle {
    position: absolute; left: 114px; top: 108px;
    width: 276px; height: 276px; border-radius: 50%;
    border: 3px solid var(--white);
    display: flex; align-items: center; justify-content: center;
  }
  .brand-circle__name {
    font-family: "Lexend", sans-serif; font-weight: 300;
    font-size: 30px; line-height: 1.25; letter-spacing: 1px;
    color: var(--white); text-align: center;
  }
</style>
</head>
<body>
<main class="canvas">

  <section class="card card--front">
    <div class="brand-name">Brook Fern Wellness</div>
    <div class="person-name">Marcus Ellery</div>
    <div class="person-title">Licensed Massage Therapist</div>

    <div class="contact-band"></div>
    <svg class="ribbon" viewBox="0 0 72 222" aria-hidden="true">
      <polygon points="8,0 64,0 72,20 0,20" fill="var(--tan-dark)"/>
      <rect x="0" y="20" width="72" height="182" fill="var(--tan)"/>
      <polygon points="0,202 72,202 64,222 8,222" fill="var(--tan-dark)"/>
    </svg>

    <ul class="contact-list">
      <li class="contact-item">
        <svg class="contact-icon" viewBox="0 0 16 16" aria-hidden="true">
          <path d="M3 1.5 L6 1.5 L7 5 L5.2 6.3 C6 8.2 7.8 10 9.7 10.8 L11 9 L14.5 10 L14.5 13 C14.5 14 13.7 14.7 12.7 14.6 C6.8 14 2 9.2 1.4 3.3 C1.3 2.3 2 1.5 3 1.5 Z" fill="var(--ink)"/>
        </svg>
        <span>321-555-0147</span>
      </li>
      <li class="contact-item">
        <svg class="contact-icon" viewBox="0 0 16 16" aria-hidden="true">
          <rect x="4" y="1" width="8" height="4" fill="var(--ink)"/>
          <rect x="1" y="6" width="14" height="6" rx="1" fill="var(--ink)"/>
          <rect x="4" y="10" width="8" height="5" fill="var(--ink)" stroke="var(--tan)" stroke-width="1"/>
        </svg>
        <span>brookfern-example.com</span>
      </li>
      <li class="contact-item">
        <svg class="contact-icon" viewBox="0 0 16 16" aria-hidden="true">
          <rect x="1" y="3" width="14" height="10" fill="var(--ink)"/>
          <polyline points="1.5,3.5 8,8.5 14.5,3.5" fill="none" stroke="var(--tan)" stroke-width="1.2"/>
        </svg>
        <span>brookfern_rest_</span>
      </li>
    </ul>
  </section>

  <section class="card card--back">
    <div class="foliage-area" role="img" aria-label="Faint oversized leafy stem decoration in soft sage tones"></div>
    <div class="brand-circle">
      <div class="brand-circle__name">Brook Fern<br>Wellness</div>
    </div>
  </section>

</main>
</body>
</html>
```